LANTERN DIVE

IM LOOKING AT A BROCHURE MY MY DIVE CENTRE WE DO COURSES FROM INTRO TO PROFESSIONAL, IM OPEN TO DESIGN AND COLOURS, JUST LOOKING FOR SOMETHING THAT STANDS OUT.

i HAVE INCLUDED A COPY OF OUR LAST BROCHURE SO YOU CAN SEE THE INFORMATION THAT WE PREVIOUSLY USED AND ALSO OUR PRICING.

WE HAVE MANY DIVE COMPANY'S IN NORTH QUEENSLAND AND THROUGHOUT AUSTRALIA, WE ARE AFTER SOMETHING THAT PEOPLE ARE DRAWN TO AND WILL STAND OUT AMONGST OTHER COMPETITORS.

LOOKING FOR PLAYFUL AND FUN

```html
<!DOCTYPE html>
<html lang="en">
<head>
<meta charset="utf-8">
<title>Lantern Dive – Tri-fold Brochure</title>
<link rel="stylesheet" href="https://fonts.googleapis.com/css2?family=Lato:ital,wght@0,400;0,700;0,900;1,700;1,900&family=Play:wght@400;700&display=swap">
<style>
  :root {
    --teal: #1fb59a;
    --teal-dark: #138f7a;
    --teal-bright: #35e0c2;
    --ocean-deep: #0e2f8f;
    --ink: #3a3a3a;
    --table-head: #2f2f2f;
    --paper: #ffffff;
    --silver-1: #f3f3f3;
    --silver-2: #cfcfcf;
    --stage: #e9e6e1;
  }
  * { box-sizing: border-box; margin: 0; padding: 0; }
  html, body { width: 1200px; height: 821px; overflow: hidden; }
  body { background: var(--stage); font-family: "Lato", sans-serif; position: relative; }

  .brochure {
    position: absolute; left: 45px; top: 16px;
    width: 1109px; height: 789px;
    display: flex;
    box-shadow: 0 6px 18px rgba(0,0,0,.25);
  }
  .panel { position: relative; height: 100%; overflow: hidden; }

  /* ---------- Left panel: course offer ---------- */
  .panel--offer {
    width: 376px;
    background: linear-gradient(180deg, #1b54c0 0%, #2e6fd3 35%, #1a44a8 60%, var(--ocean-deep) 100%);
    color: var(--paper);
  }
  .tab {
    position: absolute; top: 31px; left: 0; height: 36px;
    font-family: "Lato", sans-serif; font-weight: 900; font-size: 24px;
    line-height: 36px; padding-left: 26px; text-transform: uppercase;
  }
  .tab--light { width: 249px; background: var(--paper); color: var(--teal);
    clip-path: polygon(0 0, 100% 0, 88% 100%, 0 100%); }
  .tab--teal { width: 269px; background: var(--teal); color: var(--paper);
    clip-path: polygon(0 0, 90% 0, 100% 100%, 0 100%); padding-left: 18px; }

  .offer-title {
    position: absolute; top: 86px; left: 24px; width: 336px;
    font-weight: 900; font-style: italic; font-size: 26.5px; line-height: 31px;
    text-align: justify; text-align-last: left;
  }
  .offer-price {
    position: absolute; top: 196px; left: 24px;
    font-weight: 900; font-style: italic; font-size: 46px; color: var(--teal-bright);
  }
  .offer-schedule {
    position: absolute; top: 274px; left: 24px; width: 336px;
    font-weight: 700; font-style: italic; font-size: 21px; line-height: 30px;
  }
  .offer-schedule .days { color: var(--teal-bright); }
  .offer-call {
    position: absolute; top: 388px; left: 24px;
    font-weight: 700; font-size: 22px;
  }
  .offer-phone {
    position: absolute; top: 418px; left: 24px;
    font-weight: 400; font-size: 28px; letter-spacing: 1px; color: var(--teal-bright);
  }
  .offer-swoosh { position: absolute; left: 0; top: 450px; width: 376px; height: 339px; }

  .hours {
    position: absolute; top: 506px; left: 20px; width: 331px;
    border-collapse: separate; border-spacing: 0 3px;
    font-family: "Lato", sans-serif; color: var(--paper);
  }
  .hours th {
    background: var(--table-head); font-weight: 400; font-size: 21px;
    height: 38px; text-align: center;
  }
  .hours th:first-child { border-radius: 14px 0 0 0; width: 133px; }
  .hours th:last-child { border-radius: 0 14px 0 0; }
  .hours td {
    background: var(--teal); height: 25px; font-size: 15px; font-weight: 700;
    text-align: center; color: #0f2f2a;
  }
  .hours td:first-child { border-right: 3px solid var(--paper); }
  .hours tr:last-child td:first-child { border-radius: 0 0 0 14px; }
  .hours tr:last-child td:last-child { border-radius: 0 0 14px 0; }
  .panel-foot {
    position: absolute; left: 0; bottom: 0; width: 100%; height: 14px;
    background: #2b2b2b;
  }

  /* ---------- Middle panel: gallery & contact ---------- */
  .panel--gallery {
    width: 365px;
    background: linear-gradient(90deg, var(--silver-2) 0%, var(--silver-1) 45%, var(--silver-2) 100%);
  }
  .photo {
    position: absolute; left: 49px; width: 265px; height: 160px;
    border-radius: 26px;
    box-shadow: 0 6px 10px rgba(0,0,0,.25);
  }
  .photo--anemone { top: 88px; background: linear-gradient(135deg, #1d6a5c, #c9d24a 45%, #e1dd6a 60%, #2f7d6a); }
  .photo--clownfish { top: 262px; background: linear-gradient(135deg, #1c6fa8, #39a6c9 40%, #e58a2a 65%, #1b5f8c); }
  .photo--snapper { top: 440px; background: linear-gradient(135deg, #2a6fb6, #5fb3df 45%, #d6d94a 62%, #1d5fa0); }

  .gallery-wave { position: absolute; left: 0; top: 560px; width: 365px; height: 229px; }
  .contact {
    position: absolute; top: 654px; left: 0; width: 365px;
    text-align: center; color: var(--paper); font-size: 12.5px; line-height: 17px;
  }
  .contact svg { width: 10px; height: 10px; vertical-align: -1px; margin-right: 4px; fill: var(--paper); }
  .contact strong { font-weight: 700; }
  .website {
    position: absolute; left: 0; bottom: 14px; width: 365px; height: 36px;
    background: var(--paper); border-radius: 14px 14px 0 0;
    color: var(--teal-dark); font-weight: 700; font-size: 22px;
    text-align: center; line-height: 36px;
  }

  /* ---------- Right panel: cover ---------- */
  .panel--cover {
    width: 368px;
    background: linear-gradient(90deg, #d2d2d2 0%, #f7f7f7 50%, #d2d2d2 100%);
  }
  .cover-head {
    position: absolute; top: 0; left: 0; width: 100%; height: 148px;
    border-top: 10px solid #1aa0e8;
    text-align: center; font-family: "Play", sans-serif; color: var(--ink);
    font-size: 26px; line-height: 34px; padding-top: 18px;
  }
  .cover-head .price { color: var(--teal); font-weight: 700; font-size: 31px; }
  .cover-photo { position: absolute; left: 0; top: 148px; width: 368px; height: 540px; }
  .brand {
    position: absolute; top: 670px; left: 0; width: 100%; text-align: center;
  }
  .brand-mark {
    width: 50px; height: 50px; border-radius: 50%;
    background: var(--teal); margin: 0 auto 6px;
  }
  .brand-name { font-family: "Play", sans-serif; font-size: 23px; color: #555; }
  .brand-tagline { font-family: "Lato", sans-serif; font-size: 11px; color: var(--teal-dark); margin-top: 1px; }
</style>
</head>
<body>
<main class="brochure">

  <!-- Left panel -->
  <section class="panel panel--offer">
    <div class="tab tab--light">Get Certified</div>
    <p class="offer-title">4days open water Dive Course including 4 nights accommodation</p>
    <p class="offer-price">only $399.00</p>
    <p class="offer-schedule">Weekly courses commencing on the following days:<br><span class="days">Monday, Thursday &amp; Saturdays.</span></p>
    <p class="offer-call">Call us Today!!</p>
    <p class="offer-phone">61 400 555018</p>

    <svg class="offer-swoosh" viewBox="0 0 376 339" preserveAspectRatio="none" aria-hidden="true">
      <path d="M0 40 C110 -5 260 10 376 70 L376 339 L0 339 Z" fill="#ffffff"/>
      <path d="M0 40 C110 -5 260 10 376 70" fill="none" stroke="#1fb59a" stroke-width="6"/>
    </svg>

    <table class="hours">
      <thead><tr><th>Day</th><th>Opening Hours</th></tr></thead>
      <tbody>
        <tr><td>Monday</td><td>09:00am-4:30pm.</td></tr>
        <tr><td>Tuesday</td><td>09:00am-4:30pm.</td></tr>
        <tr><td>Wednesday</td><td>09:00am-4:30pm.</td></tr>
        <tr><td>Thrusday</td><td>09:00am-4:30pm.</td></tr>
        <tr><td>Friday</td><td>09:00am-4:30pm.</td></tr>
        <tr><td>Saturday</td><td>09:00am-4:30pm.</td></tr>
        <tr><td>Sunday</td><td>09:00am-4:30pm.</td></tr>
      </tbody>
    </table>
    <div class="panel-foot"></div>
  </section>

  <!-- Middle panel -->
  <section class="panel panel--gallery">
    <div class="tab tab--teal">Some Pictures</div>
    <div class="photo photo--anemone" role="img" aria-label="Photo of a yellow sea anemone on the reef"></div>
    <div class="photo photo--clownfish" role="img" aria-label="Photo of clownfish among coral"></div>
    <div class="photo photo--snapper" role="img" aria-label="Photo of striped reef fish in blue water"></div>

    <svg class="gallery-wave" viewBox="0 0 365 229" preserveAspectRatio="none" aria-hidden="true">
      <defs>
        <linearGradient id="waveTeal" x1="0" y1="0" x2="0" y2="1">
          <stop offset="0" stop-color="#5fd6bf"/>
          <stop offset="1" stop-color="#1a9c85"/>
        </linearGradient>
      </defs>
      <path d="M0 20 C120 70 250 70 365 50 L365 229 L0 229 Z" fill="url(#waveTeal)"/>
      <path d="M0 20 C120 70 250 70 365 50" fill="none" stroke="#ffffff" stroke-width="3"/>
    </svg>

    <div class="contact">
      <p><svg viewBox="0 0 10 10"><rect x="2" y="0" width="6" height="10" rx="1.5"/></svg>+61 400 555018</p>
      <p><svg viewBox="0 0 10 10"><rect x="0" y="2" width="10" height="7" rx="1"/></svg>info@lanterndive.com.au</p>
      <p><svg viewBox="0 0 10 10"><path d="M5 0 L10 5 L8.5 5 L8.5 10 L1.5 10 L1.5 5 L0 5 Z"/></svg>Lantern Dive</p>
      <p><strong>12 Coral Cove Rd, Palm Bay,</strong></p>
      <p><strong>Reef Island, 4870 Queensland</strong></p>
    </div>
    <div class="website">www.lanterndive.com.au</div>
    <div class="panel-foot"></div>
  </section>

  <!-- Right panel: cover -->
  <section class="panel panel--cover">
    <header class="cover-head">
      <p>Become a Certified</p>
      <p>Open Water diver for</p>
      <p class="price">ONLY $350!!</p>
    </header>

    <svg class="cover-photo" viewBox="0 0 368 540" preserveAspectRatio="none" role="img" aria-label="Photo of a scuba diver swimming beside a coral reef wall in deep blue water">
      <defs>
        <linearGradient id="sea" x1="0" y1="0" x2="1" y2="1">
          <stop offset="0" stop-color="#2a7fe0"/>
          <stop offset="0.5" stop-color="#1248b8"/>
          <stop offset="1" stop-color="#0a2f8a"/>
        </linearGradient>
      </defs>
      <path d="M0 0 L368 0 L368 365 C250 410 120 440 0 470 Z" fill="url(#sea)"/>
      <path d="M0 478 C120 448 250 418 368 375" fill="none" stroke="#1fb59a" stroke-width="6"/>
    </svg>

    <div class="brand">
      <div class="brand-mark"></div>
      <p class="brand-name">Lantern Dive</p>
      <p class="brand-tagline">Sink in, light up</p>
    </div>
    <div class="panel-foot"></div>
  </section>

</main>
</body>
</html>
```